Medigap Insurance Interactive website

We are looking at redesigning our website for a more up to date and responsive look and feel. We will code this site using Bootstrap 3 so please research and know how to design for this. Attached is our logo and a wireframe for the new site.
I look forward to seeing what you guys can do.

Target Market(s)

People elegible for Medigap Insurance in the US

Industry/Entity Type

Insurance

Number of Pages Required

5+ page

Font styles to use
Sans Serif

Requirements
Must have
• Match the logo
• Be Bootstrap 3 compatible design
• Font Awesome Icons

```html
<!DOCTYPE html>
<html lang="en">
<head>
<meta charset="utf-8">
<title>CoverWise – Medicare Supplement</title>
<link href="https://fonts.googleapis.com/css2?family=Open+Sans:wght@400;600;700&display=swap" rel="stylesheet">
<style>
:root{
  --red:#b3241c;
  --navy:#0d2f5e;
  --ink:#333;
  --muted:#666;
  --page:#f4f4f4;
  --frame:#4f4f4f;
  --line:#ddd;
  --footer:#2f2f2f;
}
*{margin:0;padding:0;box-sizing:border-box}
html,body{width:1200px;height:760px;overflow:hidden}
body{font-family:'Open Sans',sans-serif;background:var(--page);color:var(--ink);position:relative}
.site-header{position:absolute;left:0;top:0;width:1200px;height:72px;background:#fff;border-bottom:1px solid #e6e6e6}
.brand{position:absolute;left:24px;top:22px;display:flex;align-items:center;gap:7px;font-size:19px;font-weight:600;color:var(--navy)}
.brand-mark{width:12px;height:12px;background:var(--navy)}
.main-nav{position:absolute;left:174px;top:20px;display:flex;height:30px}
.main-nav a{display:flex;align-items:center;padding:0 14px;background:var(--red);color:#fff;font-size:12px;text-decoration:none;border-right:1px solid #9a1d16}
.main-nav a.active{background:var(--navy);border:0}
.main-nav a:last-child{border:0}
.contact{position:absolute;left:822px;top:19px;text-align:right;width:140px}
.contact small{display:block;font-size:11.5px;color:#222}
.contact strong{display:block;font-size:16px;font-weight:400;color:var(--red);line-height:18px}
.phone-btn{position:absolute;left:968px;top:20px;width:30px;height:30px;background:#555;display:flex;align-items:center;justify-content:center}
.social{position:absolute;left:1025px;top:20px;display:flex;gap:10px}
.social span{width:30px;height:30px;border-radius:50%;background:#ececec;border:1px solid #ddd}
.slider{position:absolute;left:23px;top:94px;width:1153px;height:288px;background:var(--frame)}
.slide{position:absolute;left:8px;top:8px;width:768px;height:272px;background:linear-gradient(135deg,#cfd6e2,#9aa6bb 55%,#e1e5ed)}
.slide h1{position:absolute;left:22px;top:22px;font-size:38px;font-weight:700;color:var(--red)}
.arrow{position:absolute;top:158px;width:20px;height:20px;border-radius:50%;background:rgba(90,90,90,.55);display:flex;align-items:center;justify-content:center}
.video{position:absolute;left:784px;top:8px;width:360px;height:272px;background:linear-gradient(160deg,#dfeaf0,#b8cfd8 60%,#eef3f5)}
.play{position:absolute;left:152px;top:108px}
.actions{position:absolute;left:24px;top:382px;width:1152px;height:47px;display:flex;background:linear-gradient(#fff,#efefef);border:1px solid #d8d8d8}
.actions a{flex:1;display:flex;align-items:center;justify-content:center;gap:6px;color:#999;font-size:17px;text-decoration:none;border-right:1px solid #d8d8d8}
.actions a:last-child{border:0}
.card{position:absolute;top:444px;width:374px;height:203px;background:#fff;border:1px solid var(--line);padding:18px 21px}
.card h2{font-size:21px;font-weight:400;color:var(--red);margin-bottom:11px}
.card p{font-size:10.4px;line-height:17.6px;color:var(--muted)}
.welcome p{text-align:justify}
.card .quote{font-size:12px;line-height:17.6px;color:#555}
.card .author{font-size:12px;color:#222;margin-top:14px;margin-left:-2px}
.dots{display:flex;gap:16px;margin-top:30px;margin-left:-2px}
.dots i{width:8px;height:8px;border-radius:50%;background:#ccc}
.dots i.on{background:var(--navy)}
.email{margin-top:10px;width:330px;height:41px;border:1px solid #ddd;background:#f6f6f6;font-size:10.4px;color:#666;padding:0 14px;display:flex;align-items:center}
.signup{margin-top:17px;display:inline-block;background:var(--navy);color:#fff;font-size:13px;padding:8px 14px}
.site-footer{position:absolute;left:0;top:664px;width:1200px;height:96px;background:var(--footer);text-align:center;color:#bbb;font-size:11px}
.footer-nav{margin-top:35px}
.footer-nav a{color:#bbb;text-decoration:none}
.footer-nav b{font-weight:400;margin:0 8px}
.copy{margin-top:10px}
</style>
</head>
<body>
<header class="site-header">
  <div class="brand"><span class="brand-mark"></span>CoverWise</div>
  <nav class="main-nav">
    <a class="active">Medicare Supplement</a><a>Part D</a><a>How to Decide</a><a>Learn Online</a><a>Why CoverWise</a><a>Buy Now</a>
  </nav>
  <div class="contact"><small>Compare Rates and Save</small><strong>(800) 555-0142</strong></div>
  <div class="phone-btn"><svg width="12" height="12" viewBox="0 0 24 24"><path fill="#fff" d="M6.6 10.8a15 15 0 0 0 6.6 6.6l2.2-2.2c.3-.3.7-.4 1-.2 1.1.4 2.3.6 3.6.6.6 0 1 .4 1 1V20c0 .6-.4 1-1 1A17 17 0 0 1 3 4c0-.6.4-1 1-1h3.5c.6 0 1 .4 1 1 0 1.3.2 2.5.6 3.6.1.3 0 .7-.2 1z"/></svg></div>
  <div class="social"><span></span><span></span><span></span><span></span></div>
</header>

<section class="slider">
  <div class="slide" role="img" aria-label="Stethoscope resting on an explanation of benefits statement">
    <h1>Why us?</h1>
    <span class="arrow" style="left:22px"><svg width="8" height="8" viewBox="0 0 10 10"><path d="M7 1 3 5l4 4" stroke="#fff" stroke-width="2" fill="none"/></svg></span>
    <span class="arrow" style="left:726px"><svg width="8" height="8" viewBox="0 0 10 10"><path d="m3 1 4 4-4 4" stroke="#fff" stroke-width="2" fill="none"/></svg></span>
  </div>
  <div class="video" role="img" aria-label="Video still of a doctor working at a laptop in a clinic">
    <svg class="play" width="56" height="56" viewBox="0 0 56 56"><circle cx="28" cy="28" r="26" fill="none" stroke="#c0281f" stroke-width="4"/><circle cx="28" cy="28" r="21" fill="#c0281f"/><path d="M22 17v22l18-11z" fill="#fff"/></svg>
  </div>
</section>

<nav class="actions">
  <a><svg width="16" height="16" viewBox="0 0 16 16"><rect x="1.5" y="4.5" width="8" height="10" fill="none" stroke="#aaa"/><rect x="6.5" y="1.5" width="8" height="10" fill="#fff" stroke="#aaa"/></svg>Compare Rates</a>
  <a><svg width="18" height="16" viewBox="0 0 18 16"><path d="M0 1h3l2 9h10l2-7H4" fill="#aaa"/><circle cx="6" cy="13.5" r="1.6" fill="#aaa"/><circle cx="14" cy="13.5" r="1.6" fill="#aaa"/></svg>Buy Now</a>
  <a><svg width="16" height="16" viewBox="0 0 16 16"><circle cx="8" cy="8" r="7" fill="#aaa"/><path d="M4 5c2 0 2 2 4 2s1 3-1 4M11 3c-1 2 1 3 3 3" stroke="#fff" fill="none"/></svg>Learn Online</a>
  <a><svg width="16" height="16" viewBox="0 0 16 16"><circle cx="8" cy="5" r="3.5" fill="none" stroke="#aaa" stroke-width="1.5"/><path d="M2 15c0-4 3-5.5 6-5.5s6 1.5 6 5.5z" fill="#aaa"/></svg>Get Expert Help</a>
</nav>

<article class="card welcome" style="left:24px">
  <h2>Welcome to CoverWise</h2>
  <p>Fusce quis placerat lorem. Phasellus lacinia nulla nibh, vel eleifend velit scelerisque vel. Sed molestie, nisl eget auctor dignissim, nibh mauris blandit nunc, non luctus arcu lorem eu urna. Quisque vel lectus faucibus, cursus felis id, mollis neque. Nunc ipsum massa, varius nec risus a, mollis aliquet mauris. Nullam metus ligula, aliquam et faucibus non, convallis et sapien. Vestibulum venenatis feugiat tortor vel suscipit. Sed eget mattis metus.</p>
</article>

<article class="card testimonials" style="left:413px">
  <h2>What People are saying</h2>
  <p class="quote">“ Quisque vel lectus faucibus, cursus felis id, mollis neque. Nunc ipsum massa, varius nec risus a, mollis aliquet mauris. Nullam metus ligula, aliquam et faucibus non. ”</p>
  <p class="author">Dana Hartley, Maple Ridge</p>
  <div class="dots"><i class="on"></i><i></i><i></i><i></i></div>
</article>

<article class="card updates" style="left:802px">
  <h2>Monthly Updates</h2>
  <p>Enter Email for customized Monthly Rate Updates and More</p>
  <div class="email">Email Address</div>
  <span class="signup">Sign Up</span>
</article>

<footer class="site-footer">
  <div class="footer-nav">
    <a>Medicare Supplement</a><b>|</b><a>Part D</a><b>|</b><a>How to Decide</a><b>|</b><a>Learn Online</a><b>|</b><a>Why CoverWise</a><b>|</b><a>Buy Now</a><b>|</b><a>CoverWise</a><b>|</b><a>Sitemap</a><b>|</b><a>Blog</a><b>|</b><a>Login</a>
  </div>
  <div class="copy">Copyright © 2016 CoverWise. All rights reserved</div>
</footer>
</body>
</html>
```